HARBOUR LEDGER Insurance Business Card Design

We need a business card designed for our personal risk / life insurance business based in Sydney Australia called 'Harbour Ledger'.

We manage and implement life insurance policies for individuals, businesses and families. Work on estate planning and succession planning. We help individuals make sure that they will be covered financially in the event of disability or critical illness.

We would like to see designs that use the colours Black, Silver/Grey , White OR different shades of Blue that are suitable for the finance / professional industries.

The final design should communicate financial safety and can also feel contemporary.
Updates

Hello,

Thanks for submitting your design.
We have recieved MANY great new designs today, thank-you.
Sorry for the late notice but for legal reasons we must include additional information of the card as follows:

Level 5, Suite 5.08,
47 Wattlebury Lane
KELBRIDGE NSW 2093

Authorised Representative No. 418730
Tallowmere Wealth Partners Pty Ltd
ABN 47 608 215 934
AFS Licence No. 572904

PLEASE REMOVE:
S marcusfellowes

PLEASE ADD:
www.harbourledger.example

Industry/Entity Type

Life Insurance

Contact Information for Business Card

Marcus Fellowes
Senior Advisor
Managing Director

M +61400 572 918
E Marcus@harbourledger.example
S marcusfellowes

Level 5, Suite 5.08
47 Wattlebury Lane
KELBRIDGE NSW 2093

Font styles to use
Serif
Sans Serif

Requirements
Must have
• - LANDSCAPE design

- MUST BE DOUBLE SIDED

Level 5, Suite 5.08,
47 Wattlebury Lane
KELBRIDGE NSW 2093

ABN 47 608 215 934
AFS Licence No. 572904

PLEASE REMOVE:
S marcusfellowes

PLEASE ADD:
www.harbourledger.example
Nice to have
• - Can have a rounded corner... but doesn't have to

```html
<!DOCTYPE html>
<html lang="en">
<head>
<meta charset="utf-8">
<title>Harbour Ledger – Business Card</title>
<link rel="stylesheet" href="https://fonts.googleapis.com/css2?family=Libre+Caslon+Text:wght@400;700&family=Open+Sans:wght@400;600&display=swap">
<style>
  :root{
    --bg:#c9cccd;
    --card:#f4f4f4;
    --red:#b3001b;
    --red-deep:#8c0014;
    --grey:#8e8e8e;
    --ink:#2a2a2a;
    --white:#ffffff;
  }
  *{box-sizing:border-box;margin:0;padding:0}
  html,body{width:1200px;height:1000px;overflow:hidden}
  body{background:var(--bg);position:relative;font-family:"Open Sans",sans-serif}
  .card{position:absolute;width:760px;height:434px;background:var(--card);border-radius:6px;overflow:hidden;box-shadow:0 8px 22px rgba(0,0,0,.25)}
  .card svg.shapes{position:absolute;inset:0}
  .card--front{left:380px;top:40px}
  .card--back{left:60px;top:526px}
  .wordmark{position:absolute;display:flex;align-items:center;gap:16px;font-family:"Libre Caslon Text",serif;font-weight:400;letter-spacing:1px;white-space:nowrap}
  .wordmark__square{display:block}
  .card--front .wordmark{left:0;right:0;top:150px;justify-content:center;font-size:40px;color:var(--ink)}
  .card--front .wordmark__square{width:64px;height:64px;background:var(--ink)}
  .card--back .wordmark{left:40px;top:58px;font-size:32px;color:var(--grey)}
  .card--back .wordmark__square{width:54px;height:54px;background:var(--grey)}
  .holder{position:absolute;left:96px;top:240px;color:var(--red);white-space:nowrap}
  .holder__name{font-size:44px;font-weight:400;line-height:1.1}
  .holder__title{font-size:21px;font-weight:600;margin-top:4px}
  .contact{position:absolute;left:526px;top:48px;width:226px;color:var(--white);list-style:none}
  .contact li{display:flex;align-items:flex-start;gap:9px;margin-bottom:17px;white-space:nowrap}
  .contact svg{flex:none;width:17px;height:17px;margin-top:1px}
  .contact__address{font-family:"Libre Caslon Text",serif;font-weight:700;font-size:11px;line-height:1.5}
  .contact__item{font-size:14px}
  .contact__item--small{font-size:12.5px}
  .legal{position:absolute;left:526px;top:318px;width:226px;color:var(--white);font-size:10.5px;line-height:1.55;white-space:nowrap;opacity:.92}
</style>
</head>
<body>

<section class="card card--front" aria-label="Card front">
  <svg class="shapes" width="760" height="434" viewBox="0 0 760 434">
    <path fill="var(--red)" d="M250,0 H440 V10 Q440,24 426,24 H264 Q250,24 250,10 Z"/>
    <rect fill="var(--red)" x="0" y="330" width="760" height="104"/>
    <path fill="var(--card)" d="M220,320 V356 Q220,372 236,372 H404 Q420,372 420,356 V320 Z"/>
  </svg>
  <div class="wordmark"><span class="wordmark__square"></span>HARBOUR LEDGER</div>
</section>

<section class="card card--back" aria-label="Card back">
  <svg class="shapes" width="760" height="434" viewBox="0 0 760 434">
    <path fill="var(--red)" d="M0,200 H30 Q52,200 52,222 V412 Q52,434 30,434 H0 Z"/>
    <path fill="var(--red-deep)" d="M470,0 H760 V434 H470 V254 Q470,240 484,240 H496 Q510,240 510,226 V54 Q510,40 496,40 H484 Q470,40 470,26 Z"/>
  </svg>
  <div class="wordmark"><span class="wordmark__square"></span>HARBOUR LEDGER</div>
  <div class="holder">
    <p class="holder__name">Marcus Fellowes</p>
    <p class="holder__title">Senior Advisor Managing Director</p>
  </div>
  <ul class="contact">
    <li>
      <svg viewBox="0 0 20 20"><path fill="none" stroke="#fff" stroke-width="2" d="M10,18 C5,12 4,10 4,8 a6,6 0 0 1 12,0 c0,2 -1,4 -6,10 Z"/><circle cx="10" cy="8" r="2" fill="#fff"/></svg>
      <span class="contact__address">Level 5, Suite 5.08,<br>47 Wattlebury Lane<br>KELBRIDGE NSW 2093</span>
    </li>
    <li>
      <svg viewBox="0 0 20 20"><path fill="#fff" d="M5,2 L8,2 L9,6 L7,8 Q9,12 12,13 L14,11 L18,12 L18,15 Q18,18 15,18 Q3,16 2,5 Q2,2 5,2 Z"/></svg>
      <span class="contact__item">+61400 572 918</span>
    </li>
    <li>
      <svg viewBox="0 0 20 20"><rect x="2" y="5" width="16" height="11" fill="none" stroke="#fff" stroke-width="2"/><path d="M2,5 L10,11 L18,5" fill="none" stroke="#fff" stroke-width="2"/></svg>
      <span class="contact__item contact__item--small">Marcus@harbourledger.example</span>
    </li>
    <li>
      <svg viewBox="0 0 20 20"><circle cx="10" cy="10" r="7" fill="none" stroke="#fff" stroke-width="2"/><circle cx="10" cy="10" r="2.5" fill="#fff"/></svg>
      <span class="contact__item contact__item--small">www.harbourledger.example</span>
    </li>
  </ul>
  <div class="legal">
    <p>Authorised Representative No. 418730</p>
    <p>Tallowmere Wealth Partners Pty Ltd</p>
    <p>ABN 47 608 215 934</p>
    <p>AFS Licence No. 572904</p>
  </div>
</section>

</body>
</html>
```